Letter Head- Window Cleaning Industry

Need a letter head for 'Fernbrook Window Cleaning'. We provide a premium residential & commercial window cleaning service to Melbourne and surrounding suburbs.
Would like a design similar to the flyer, logo and uniform attached. The final design should communicate trust and quality.
Address is 1204/58 Haldane St, Southmere Victoria 3141. The rest of the information is on the flyer.
*Please note the Phone number on the uniform designs is incorrect.

Thank-you very much!

Industry/Entity Type

Window Cleaning

```html
<!DOCTYPE html>
<html lang="en">
<head>
<meta charset="utf-8">
<title>Fernbrook Window Cleaning – Letterhead</title>
<link rel="stylesheet" href="https://fonts.googleapis.com/css2?family=Roboto+Condensed:wght@400;700&display=swap">
<style>
  :root {
    --backdrop: #e9e6e1;
    --paper: #ffffff;
    --orange-deep: #e99a2c;
    --orange-mid: #f2b962;
    --orange-pale: #fbe6c6;
    --ink: #222222;
    --ink-soft: #555555;
    --footer-band: #3d3d3f;
    --footer-text: #cfcfcf;
    --skyline-dark: #c9c9c9;
    --skyline-mid: #dcdcdc;
    --watermark: #f4f4f4;
  }
  * { box-sizing: border-box; margin: 0; padding: 0; }
  html, body { width: 1200px; height: 1000px; overflow: hidden; }
  body {
    background: var(--backdrop);
    font-family: "Roboto Condensed", Arial, sans-serif;
    position: relative;
  }
  .letterhead {
    position: absolute;
    left: 282px; top: 50px;
    width: 636px; height: 900px;
    background: var(--paper);
    box-shadow: 0 6px 22px rgba(0,0,0,0.18);
    overflow: hidden;
  }
  .header-glow {
    position: absolute; left: 0; top: 0;
    width: 100%; height: 260px;
    background:
      linear-gradient(to bottom, rgba(255,255,255,0) 55%, var(--paper) 100%),
      linear-gradient(160deg, rgba(255,255,255,0) 18%, var(--orange-pale) 42%, var(--orange-mid) 68%, var(--orange-deep) 100%);
  }
  .brand-tile {
    position: absolute; left: 26px; top: 16px;
    width: 188px; height: 74px;
    background: #f7f1e6;
    border-radius: 8px;
    display: flex; align-items: center; justify-content: center; gap: 8px;
  }
  .brand-tile .brand-mark { width: 12px; height: 12px; background: var(--ink); }
  .brand-tile .brand-name {
    font-weight: 700; font-size: 22px; letter-spacing: 1px;
    color: var(--ink); text-transform: uppercase;
  }
  .company-block {
    position: absolute; right: 26px; top: 150px;
    text-align: right; color: var(--ink);
  }
  .company-block .company-name {
    font-weight: 700; font-size: 10.5px; letter-spacing: 0.6px;
    text-transform: uppercase;
    padding-bottom: 4px; border-bottom: 1px solid var(--ink-soft);
  }
  .company-block .address {
    margin-top: 6px; font-size: 10.5px; line-height: 1.35; color: var(--ink-soft);
  }
  .skyline-area {
    position: absolute; left: 0; bottom: 44px;
    width: 100%; height: 250px;
    background:
      linear-gradient(to bottom, var(--paper) 0%, rgba(255,255,255,0) 40%),
      linear-gradient(to right, var(--skyline-mid) 0%, var(--skyline-dark) 35%, var(--skyline-mid) 65%, #e6e6e6 100%);
  }
  .watermark-name {
    position: absolute; left: 22px; bottom: 92px;
    font-weight: 700; font-size: 56px; letter-spacing: 2px;
    color: var(--watermark); text-transform: uppercase;
  }
  .footer-band {
    position: absolute; left: 0; bottom: 0;
    width: 100%; height: 44px;
    background: var(--footer-band);
    display: flex; align-items: center; justify-content: space-between;
    padding: 0 24px;
    color: var(--footer-text); font-size: 12.5px; letter-spacing: 0.3px;
  }
</style>
</head>
<body>
  <main class="letterhead">
    <div class="header-glow" role="img" aria-label="Soft orange light swoosh across the top of the page"></div>

    <div class="brand-tile">
      <span class="brand-mark"></span>
      <span class="brand-name">Fernbrook</span>
    </div>

    <section class="company-block">
      <p class="company-name">Fernbrook Window Cleaning</p>
      <p class="address">1204/58 Haldane St,<br>Southmere Victoria<br>3141</p>
    </section>

    <div class="skyline-area" role="img" aria-label="Faint grey city skyline silhouette along the bottom of the page"></div>
    <p class="watermark-name">Fernbrook</p>

    <footer class="footer-band">
      <span class="phone">8421 0937</span>
      <span class="website">www.fernbrookwindows.com.au</span>
      <span class="email">info@fernbrookwindows.com.au</span>
    </footer>
  </main>
</body>
</html>
```